Business Card Design Project for Electrical Company

We need a business card designed for a new Electrical Company called Venrol Electrical Solutions, i dont mind if only Venrol Electrical is used. We are a domestic and commercial Electrical Company that provides a range of Electrical Services. Our Company colours are Fluro Yellow and Black with the Lightning bolt picture attached.I have attached a card that has been made i think it is rather basic and am looking for something more. the font of Venrol Electrical has been used on our car graphics as well as the lightning bolt. i want to keep them the same so we can brand our business. Some things we want on the front of the card are Venrol Electrical Solutions, Derek Pollard, 0438562917, admin@venrolelectrical.example, Lic No 58342, Servicing CQ Region. But we want Dereks name seperate to the phone number as its the phone number for the office, derek wont be answering the phone so we are thinking we dont want to give that impression. What do you think? with all that if you have complete different font designs please submit what you think would work best. keeping in mind our company name and details as well as coulors.

Industry/Entity Type

Business

```html
<!DOCTYPE html>
<html lang="en">
<head>
<meta charset="utf-8">
<title>Venrol Electrical Solutions – Business Card</title>
<link rel="stylesheet" href="https://fonts.googleapis.com/css2?family=Open+Sans:wght@300;400;600;700&display=swap">
<style>
  :root {
    --fluro: #dfe80c;
    --ink: #1b1b1b;
    --ink-soft: #2c2c2c;
    --paper: #ffffff;
    --grey-text: #555555;
    --muted: #8a8a8a;
    --stage: #e9e7e3;
    --font-main: "Open Sans", Arial, sans-serif;
  }
  * { box-sizing: border-box; margin: 0; padding: 0; }
  html, body {
    width: 1200px; height: 1023px; overflow: hidden;
    background: var(--stage);
    font-family: var(--font-main);
  }
  .stage { position: relative; width: 1200px; height: 1023px; }

  .card {
    position: absolute; left: 230px; width: 740px; height: 420px;
    overflow: hidden; border-radius: 4px;
    box-shadow: 0 10px 28px rgba(0,0,0,0.22);
  }
  .card-front { top: 70px; background: var(--paper); }
  .card-back {
    top: 533px;
    background: linear-gradient(160deg, var(--ink-soft) 0%, var(--ink) 70%);
  }

  .swoosh { position: absolute; inset: 0; width: 100%; height: 100%; }

  .bolt-area { position: absolute; border-radius: 50%; }
  .card-front .bolt-area {
    left: 60px; top: 170px; width: 260px; height: 200px;
    background: radial-gradient(ellipse at center, rgba(170,170,170,0.35) 0%, rgba(255,255,255,0) 70%);
  }
  .card-back .bolt-area {
    left: 170px; top: 40px; width: 320px; height: 280px;
    background: radial-gradient(ellipse at center, rgba(230,230,230,0.22) 0%, rgba(30,30,30,0) 70%);
  }

  .brand-name {
    position: absolute;
    font-family: var(--font-main); font-weight: 700;
    text-transform: uppercase;
    line-height: 1.02; letter-spacing: 0.5px;
  }
  .card-front .brand-name { left: 90px; top: 222px; font-size: 30px; color: var(--ink); }
  .card-back .brand-name { left: 190px; top: 120px; font-size: 44px; color: var(--fluro); }

  .contact {
    position: absolute; left: 345px; top: 78px; width: 300px; color: var(--ink);
  }
  .contact .person-name { font-size: 26px; font-weight: 600; }
  .contact .person-role { font-size: 12px; color: var(--muted); margin-top: 2px; }
  .contact .divider {
    width: 70px; height: 2px; background: var(--fluro); margin: 18px 0 14px;
  }
  .contact .detail { font-size: 14px; line-height: 1.75; color: var(--grey-text); white-space: nowrap; }
  .contact .detail-label { color: var(--ink); }

  .services-band {
    position: absolute; left: 0; right: 0; bottom: 0; height: 84px;
    background: var(--fluro);
    display: grid; grid-template-columns: repeat(4, 1fr); grid-template-rows: 1fr 1fr;
    padding: 14px 36px; align-items: center;
  }
  .service { font-size: 14px; color: var(--ink); }
</style>
</head>
<body>
<main class="stage">

  <section class="card card-front" aria-label="Card front">
    <svg class="swoosh" viewBox="0 0 740 420" preserveAspectRatio="none" aria-hidden="true">
      <path d="M0 0 H740 V18 C520 10 260 40 0 120 Z" fill="var(--fluro)"/>
      <path d="M0 0 H740 V8 C520 0 260 28 0 100 Z" fill="var(--paper)" transform="translate(0,-2)"/>
      <path d="M740 150 C690 280 560 380 380 420 H740 Z" fill="var(--ink)"/>
      <path d="M740 120 C680 270 540 380 330 420 H380 C560 380 690 280 740 150 Z" fill="var(--fluro)"/>
    </svg>
    <div class="bolt-area" role="img" aria-label="Faint grey lightning bolt artwork"></div>
    <div class="brand-name">Venrol<br>Electrical<br>Solutions</div>
    <div class="contact">
      <p class="person-name">Derek Pollard</p>
      <p class="person-role">Licensed Electrician</p>
      <div class="divider"></div>
      <p class="detail">Lic No 58342, Servicing CQ</p>
      <p class="detail"><span class="detail-label">Phone:</span> 0438562917</p>
      <p class="detail"><span class="detail-label">Email:</span> admin@venrolelectrical.example</p>
    </div>
  </section>

  <section class="card card-back" aria-label="Card back">
    <div class="bolt-area" role="img" aria-label="White lightning bolt artwork"></div>
    <div class="brand-name">Venrol<br>Electrical<br>Solutions</div>
    <div class="services-band">
      <span class="service">Light &amp; Power</span>
      <span class="service">Design &amp; Installation</span>
      <span class="service">TV &amp; Data</span>
      <span class="service">Renovations</span>
      <span class="service">Test &amp; Tagging</span>
      <span class="service">Air Con Installation</span>
      <span class="service">Residential</span>
      <span class="service">Smoke Detectors</span>
    </div>
  </section>

</main>
</body>
</html>
```